I need a brochure for my new company "Nine Moons". You can read all about the company at http://www.ninemoons-example.com.sg
On the website you will also get an idea of the concept of the product, as well as design. This design actually comes from a Wordpress theme.
The brochure needs to be like a print version of the website but much more summarised, high-level. I'd like to distribute it to expecting mothers at various locations such as pre-natal yoga classes. The intention is to create enough interest so these moms-to-be will surf to my website and check out what it's all about.
Target Market(s)
Expecting moms and dads (pregnant)
Industry/Entity Type
It Company
Look and feel
Each slider illustrates characteristics of the customer's brand and the style your logo design should communicate.

```html
<!DOCTYPE html>
<html lang="en">
<head>
<meta charset="utf-8">
<title>Nine Moons – Brochure Spread</title>
<link href="https://fonts.googleapis.com/css2?family=Oswald:wght@300;400;500&family=Raleway:wght@300;400;600;700&display=swap" rel="stylesheet">
<style>
  :root {
    --backdrop: #e7e4e0;
    --paper: #ffffff;
    --teal: #5cc3cc;
    --teal-light: #8fd6dc;
    --teal-dark: #2f9aa5;
    --ink: #55595d;
    --ink-soft: #7b8086;
    --heading-grey: #9aa3ab;
    --bullet: #6ccad2;
  }
  * { margin: 0; padding: 0; box-sizing: border-box; }
  html, body { width: 1200px; height: 880px; overflow: hidden; background: var(--backdrop); }
  body { position: relative; font-family: "Raleway", sans-serif; color: var(--ink); }

  .spread {
    position: absolute; left: 50px; top: 46px; width: 1100px; height: 785px;
    background: var(--paper);
    box-shadow: 0 4px 14px rgba(0,0,0,.12);
  }
  .fold {
    position: absolute; left: 556px; top: 0; width: 1px; height: 100%;
    background: linear-gradient(to bottom, #eceef0, #e2e5e8, #eceef0);
  }

  /* left page */
  .ribbon { position: absolute; left: 0; top: 38px; width: 412px; height: 76px; }
  .ribbon-title {
    position: absolute; left: 50px; top: 55px; width: 290px; text-align: center;
    font-family: "Oswald", sans-serif; font-weight: 400; font-size: 17.5px;
    color: #fff; letter-spacing: .1px; text-transform: uppercase; white-space: nowrap;
  }
  .intro {
    position: absolute; left: 71px; top: 140px; width: 416px;
    font-size: 12.6px; line-height: 17px; font-weight: 400; color: var(--ink-soft);
    text-align: justify;
  }
  .intro p + p { margin-top: 12px; }
  .tagline {
    position: absolute; left: 71px; top: 311px; width: 416px; text-align: center;
    font-size: 22px; font-weight: 300; color: var(--teal);
  }
  .booties-photo {
    position: absolute; left: 67px; top: 375px; width: 413px; height: 197px;
    border-radius: 40px;
    background: radial-gradient(ellipse at 30% 55%, #b7d3e6 0%, #d3e4ef 35%, rgba(255,255,255,0) 60%),
                radial-gradient(ellipse at 70% 50%, #f2c9cd 0%, #f7dfe1 35%, rgba(255,255,255,0) 62%);
  }
  .about {
    position: absolute; left: 71px; top: 627px; width: 410px;
    font-size: 13.4px; line-height: 17.5px; color: var(--ink);
  }
  .about strong { font-weight: 700; }

  /* right page */
  .services-title {
    position: absolute; left: 603px; top: 38px;
    font-family: "Oswald", sans-serif; font-weight: 400; font-size: 24px;
    color: var(--heading-grey); letter-spacing: .5px;
  }
  .phase {
    position: absolute; left: 603px;
    font-size: 18px; font-weight: 300; color: var(--teal);
  }
  .phase-pregnancy { top: 85px; }
  .phase-after { top: 343px; }
  .service-list { position: absolute; list-style: none; }
  .service-list li {
    position: relative; padding-left: 22px; font-size: 13px; line-height: 16px;
    color: var(--ink-soft); white-space: nowrap;
  }
  .service-list li::before {
    content: ""; position: absolute; left: 0; top: 4px; width: 10px; height: 10px;
    background: linear-gradient(135deg, var(--teal-light), var(--bullet));
  }
  .list-pregnancy-a { left: 603px; top: 124px; }
  .list-pregnancy-a li { margin-bottom: 13.5px; }
  .list-pregnancy-b { left: 860px; top: 124px; width: 180px; }
  .list-pregnancy-b li { margin-bottom: 13.5px; }
  .list-after { left: 603px; top: 377px; }
  .list-after li { margin-bottom: 16px; padding-left: 24px; }

  .contact {
    position: absolute; left: 833px; top: 378px; width: 240px; text-align: center;
  }
  .contact .label { font-size: 11.5px; font-weight: 700; color: var(--teal); }
  .contact .url {
    font-size: 15.5px; font-weight: 400; color: var(--heading-grey);
    margin: 6px 0 2px; letter-spacing: .2px; white-space: nowrap;
  }
  .contact .phone { font-size: 29px; font-weight: 400; color: var(--teal); margin-top: 12px; letter-spacing: .5px; }

  .meet {
    position: absolute; left: 622px; top: 556px; width: 478px; height: 183px;
    border-radius: 10px 0 0 10px;
    background: linear-gradient(to bottom, #80d2d8 0%, #6ccad1 55%, #5ec2ca 100%);
    box-shadow: 0 14px 16px -10px rgba(0,0,0,.35);
  }
  .meet-photo {
    position: absolute; left: 9px; top: 13px; width: 115px; height: 157px;
    border-radius: 10px; border: 3px solid #fff;
    background: linear-gradient(160deg, #d9cfc6 0%, #efe9e4 45%, #f7f5f2 100%);
  }
  .meet-title {
    position: absolute; left: 150px; top: 20px;
    font-family: "Oswald", sans-serif; font-weight: 400; font-size: 22px;
    color: #fff; text-transform: uppercase; letter-spacing: .4px;
  }
  .meet-text {
    position: absolute; left: 150px; top: 61px; width: 305px;
    font-size: 11.6px; line-height: 16px; font-weight: 700; color: #fff;
  }
</style>
</head>
<body>
  <main class="spread">
    <div class="fold"></div>

    <section class="page page-left">
      <svg class="ribbon" viewBox="0 0 412 76" aria-hidden="true">
        <polygon points="330,20 412,20 390,47 412,74 330,74" fill="#3fb0bb"/>
        <polygon points="0,0 363,0 363,60 0,60" fill="#71cdd4"/>
        <polygon points="363,60 330,60 363,74" fill="#2a8a94"/>
        <line x1="0" y1="5" x2="363" y2="5" stroke="#ffffff" stroke-opacity=".7" stroke-dasharray="4 3"/>
        <line x1="0" y1="55" x2="363" y2="55" stroke="#ffffff" stroke-opacity=".7" stroke-dasharray="4 3"/>
      </svg>
      <h1 class="ribbon-title">Congratulations, you're expecting!</h1>

      <div class="intro">
        <p>While endless joy awaits you at the end of nine months, a mountain of tasks is slowly but steadily piling up in anticipation of your little one. And questions, so many questions that your doctor/midwife just can't answer for you!</p>
        <p>What do I need to buy to prepare for this baby? Essential vs. nice to have? I need to start planning the baby shower&nbsp; invites, decoration, food, lots to do&nbsp; How should I decorate the nursery? What about a confinement nanny, and planning the first-month celebration? Have I thought about a birth plan? I need to start researching hospitals...</p>
      </div>

      <h2 class="tagline">So much to do and think about!</h2>

      <div class="booties-photo" role="img" aria-label="Photo of a pair of blue and a pair of pink knitted baby booties"></div>

      <p class="about"><strong>Nine Moons</strong> is a Baby Planning &amp; Maternity Concierge that lets busy moms and dads relax while we take care of all the planning. First-time parents are relieved for the guidance, and experienced parents just appreciate the extra set of hands and brains!</p>
    </section>

    <section class="page page-right">
      <h2 class="services-title">SERVICES</h2>

      <h3 class="phase phase-pregnancy">During your pregnancy...</h3>
      <ul class="service-list list-pregnancy-a">
        <li>The Nine Month Action Plan</li>
        <li>Product reviews and suggestions</li>
        <li>Nursery Setup &amp; Design</li>
        <li>Layette Shopping</li>
        <li>Baby Shower Planning</li>
        <li>Sourcing for Confinement Nanny</li>
        <li>Newborn Care</li>
      </ul>
      <ul class="service-list list-pregnancy-b">
        <li>Baby Registry Setup</li>
        <li>Birth Planning</li>
        <li>Baby Announcement</li>
        <li>Health, Happiness &amp; Well<br>-Being</li>
        <li>Advice &amp; Consultation</li>
        <li>Concierge Service</li>
      </ul>

      <h3 class="phase phase-after">After birth...</h3>
      <ul class="service-list list-after">
        <li>Newborn Care (up to 12 mths)</li>
        <li>Postpartum Support</li>
        <li>Asian Confinement Traditions</li>
        <li>Nanny / Childcare Sourcing</li>
        <li>Baby Food Making</li>
      </ul>

      <div class="contact">
        <p class="label">for more informations go to</p>
        <p class="url">www.ninemoons-example.com.sg</p>
        <p class="label">or call me</p>
        <p class="phone">8000-1234</p>
      </div>

      <div class="meet">
        <div class="meet-photo" role="img" aria-label="Photo of an expecting mother relaxing on a bed while on the phone"></div>
        <h3 class="meet-title">Let's meet</h3>
        <p class="meet-text">The first thing I do is a free telephone or face-to-face consultation at a location of your choice, be that your home, or somewhere we can grab a coffee together. The idea is to get to know you and your pregnancy better, and find out your needs and goals as well as your budget.</p>
      </div>
    </section>
  </main>
</body>
</html>
```